New Web Design Project- Willowbrook Elders

Willowbrook Elders is the Capital regions premiere, non-medical, in-home care & companionship service that unites "junior-senior" caregivers with "senior-senior" care recipients so that senior-seniors can remain safe & independent in their own homes.
Our compassionate "junior-senior" caregivers are all retirees that have already enjoyed rewarding careers and/or have raised families of their own and feel the need to pay-it-forward with their care for older seniors.
Services include grocery shopping, medical or dental appointments, errands, meal preparation & cleanup, light housekeeping, bed making, laundry, hobbies, reading, transportation, entertainment, games, mobility assistance/transfers, respite care, light yard work, pet walking.

Target Market(s)

Grown children of senior-seniors between who are between 55-70, predominantly the daughters (female). End users of services (senior-seniors) are typically 80-100 years old and living in own homes

Industry/Entity Type

Medical

Coding

Coded - Design and coding required

Number of Pages Required

5+ page

Font styles to use
Sans Serif

Colors
3277b5
ec1f27

Requirements
Must have
• supporting photos on each page. Contact us page. Promotional video (done) attached that doesn't take viewers off my site (https://vidhost.example/q7Rk2mPzL4n).
• Also, need my downloadable brochure (attached).
• The following pages:
• Home. Services. About Us. News. Employment. Contact us. Junior-Seniors Assisting Senior-Seniors. Why non-medical in-home care. Who are junior-seniors?Financial effects of senior care. Do you need care? Does someone you love need care?
Should not have
• Any other photos or images other than what I've supplied.

```html
<!DOCTYPE html>
<html lang="en">
<head>
<meta charset="utf-8">
<title>Willowbrook Elders</title>
<link href="https://fonts.googleapis.com/css2?family=Montserrat:wght@300;400;500;600;700&display=swap" rel="stylesheet">
<style>
:root{
  --navy:#0e4a8b;
  --navy-dark:#0a3a70;
  --coral:#f05a52;
  --ink:#333;
  --light:#f4f4f4;
  --white:#fff;
}
*{box-sizing:border-box;margin:0;padding:0}
html,body{width:1200px;height:3888px;overflow:hidden}
body{font-family:"Montserrat",Arial,sans-serif;color:var(--ink);background:var(--white);position:relative}
a{color:inherit;text-decoration:none}

/* header */
.site-header{position:absolute;top:0;left:0;width:1200px;height:104px;background:var(--white)}
.brand{position:absolute;left:98px;top:30px;display:flex;align-items:center;gap:12px}
.brand-square{width:30px;height:30px;background:var(--navy)}
.brand-name{font-size:26px;font-weight:600;color:var(--navy)}
.header-phone{position:absolute;right:98px;top:38px;font-size:22px;color:#2f74b5}
.main-nav{position:absolute;top:104px;left:0;width:1200px;height:31px;background:var(--coral);display:flex;justify-content:center}
.main-nav a{color:var(--white);font-size:13px;font-weight:600;line-height:31px;padding:0 36px}

/* hero */
.hero{position:absolute;top:135px;left:0;width:1200px;height:435px;background:var(--navy)}
.hero-text{position:absolute;left:186px;top:96px;color:var(--white);font-size:40px;font-weight:300;line-height:61px;letter-spacing:1px}
.hero-text b{font-weight:700}
.hero-photo{position:absolute;left:588px;top:0;width:612px;height:435px;background:linear-gradient(135deg,#9fb17c,#e6d7cf 55%,#c9a4b5)}

/* intro */
.video-box{position:absolute;left:98px;top:614px;width:573px;height:228px;background:var(--navy)}
.video-box .vb-name{position:absolute;left:0;right:0;top:50px;text-align:center;color:var(--white);font-size:34px;font-weight:500}
.video-btn{position:absolute;left:138px;top:136px;width:317px;height:58px;background:var(--coral);color:var(--white);display:flex;align-items:center;gap:14px;padding-left:18px;font-size:19px;line-height:22px}
.brochure{position:absolute;left:697px;top:614px;width:402px;height:228px;background:var(--coral)}
.brochure-title{position:absolute;left:16px;top:78px;color:var(--white);font-size:25px;font-weight:600;line-height:40px}
.brochure-thumb{position:absolute;right:0;top:0;width:170px;height:228px;background:linear-gradient(160deg,#e9dfe2,#b9a6bd 60%,#3f5b94)}

.topic{position:absolute;width:318px}
.topic h3{font-size:19px;font-weight:500;color:var(--coral);line-height:26px}
.topic p{font-size:13px;line-height:21px;color:#444;margin-top:16px}
.btn-learn{position:absolute;width:318px;height:33px;background:var(--navy);color:var(--white);font-size:12px;text-align:center;line-height:33px}

/* services */
.services{position:absolute;top:1400px;left:0;width:1200px;height:427px;background:var(--navy);color:var(--white)}
.section-title{position:absolute;left:0;width:1200px;text-align:center;font-size:31px;font-weight:400}
.rule{position:absolute;left:520px;width:160px;height:1px}
.rule::after{content:"";position:absolute;left:77px;top:-3px;width:6px;height:6px;border-radius:50%;background:var(--coral)}
.service{position:absolute;top:130px;width:250px;text-align:center}
.service .hex{margin:0 auto;display:block}
.service h4{font-size:12px;font-weight:500;margin-top:22px;line-height:16px}
.service p{font-size:12px;line-height:18px;margin-top:12px}
.dots{position:absolute;top:366px;left:554px;display:flex;gap:9px}
.dots span{width:15px;height:15px;border-radius:50%;background:var(--white)}
.dots span.on{background:var(--coral);border:3px solid var(--white)}

/* testimonial */
.testimonial{position:absolute;top:1827px;left:0;width:1200px;height:381px;background:var(--white)}
.t-photo{position:absolute;left:158px;top:88px;width:228px;height:267px;background:linear-gradient(180deg,#8a8d92,#4a4e56)}
.t-card{position:absolute;left:386px;top:101px;width:627px;height:239px;background:var(--white);box-shadow:0 4px 14px rgba(0,0,0,.22)}
.t-quote{position:absolute;left:74px;top:58px;width:480px;font-size:13px;line-height:21px;color:#555}
.t-author{position:absolute;left:74px;top:178px;display:flex;align-items:center;gap:10px;font-size:13px}
.t-author i{width:70px;height:1px;background:var(--coral)}
.t-author b{color:var(--coral);font-weight:500;font-size:15px}

/* news */
.news{position:absolute;top:2208px;left:0;width:1200px;height:742px;background:var(--navy);color:var(--white)}
.news-grid{position:absolute;left:98px;top:117px;width:1001px;height:498px;display:grid;grid-template-columns:repeat(4,1fr);grid-template-rows:repeat(2,1fr)}
.news-item{background:var(--coral);padding:56px 16px 0 12px;font-size:13px;line-height:21px;position:relative}
.news-item time{display:block;margin-bottom:16px}
.news-item::after{content:"";position:absolute;right:-12px;top:100px;border:12px solid transparent;border-left-color:var(--coral);border-right:0;z-index:2}
.news-item.left-arrow::after{right:auto;left:-12px;border-left:0;border-right:12px solid var(--coral)}
.news-photo{background:linear-gradient(140deg,#d9d2c9,#8f7c6d)}
.news-photo.b{background:linear-gradient(140deg,#b5c69a,#e4d9d6)}
.news-photo.c{background:linear-gradient(140deg,#c8a57a,#e8e1d8)}
.news-photo.d{background:linear-gradient(140deg,#9fa7b3,#e2d6c9)}
.btn-more{position:absolute;left:531px;top:659px;width:138px;height:36px;background:var(--coral);color:var(--white);font-size:13px;font-weight:600;text-align:center;line-height:36px}

/* contact */
.contact{position:absolute;top:2950px;left:0;width:1200px;height:640px;background:var(--light)}
.contact .section-title{top:40px;color:#555;font-size:32px}
.contact-sub{position:absolute;top:96px;left:0;width:1200px;text-align:center;font-size:12px;color:#999}
.map{position:absolute;left:98px;top:178px;width:407px;height:426px;background:linear-gradient(160deg,#e4ebd8,#f2efe6 50%,#dfe6d6)}
.contact-form{position:absolute;left:529px;top:178px;width:570px;height:426px;background:var(--white);box-shadow:0 2px 8px rgba(0,0,0,.12)}
.field{position:absolute;left:86px;width:400px;border-bottom:1px solid #ddd;font-size:12px;color:#888;padding-bottom:12px}
.btn-send{position:absolute;left:86px;top:328px;width:136px;height:36px;background:var(--coral);color:var(--white);font-size:12px;font-weight:600;text-align:center;line-height:36px}

/* footer */
.site-footer{position:absolute;top:3590px;left:0;width:1200px;height:267px;background:var(--navy);color:var(--white)}
.footer-h{position:absolute;font-size:14px;font-weight:600}
.quick-links{position:absolute;left:98px;top:62px;width:230px;list-style:none}
.quick-links li{font-size:12px;height:31px;line-height:30px;border-bottom:1px solid rgba(255,255,255,.15)}
.quick-links li::before{content:"› "}
.address{position:absolute;left:502px;top:72px;font-size:13px;line-height:20px}
.address strong{font-size:14px;font-weight:600}
.contact-line{display:flex;align-items:center;gap:10px;margin-top:14px}
.footer-brand{position:absolute;right:98px;top:108px;display:flex;align-items:center;gap:10px}
.footer-brand .brand-square{background:var(--white)}
.footer-brand .brand-name{color:var(--white);font-size:22px}
.copyright{position:absolute;top:3857px;left:0;width:1200px;height:31px;background:var(--navy-dark);color:var(--white);font-size:11px;text-align:center;line-height:31px}
</style>
</head>
<body>

<header class="site-header">
  <div class="brand"><span class="brand-square"></span><span class="brand-name">Willowbrook Elders</span></div>
  <div class="header-phone">Call (555)-014-2290 Today!</div>
</header>
<nav class="main-nav">
  <a href="#">Home</a><a href="#">Services</a><a href="#">About Us</a><a href="#">News</a><a href="#">Employment</a><a href="#">Contact us</a>
</nav>

<section class="hero">
  <h1 class="hero-text">The care<br>and <b>company</b><br>you need<br>to be at <b>home</b></h1>
  <div class="hero-photo" role="img" aria-label="Photo of two smiling senior women sitting together outdoors"></div>
</section>

<section class="intro">
  <a class="video-box" href="https://vidhost.example/q7Rk2mPzL4n">
    <div class="vb-name">Willowbrook Elders</div>
    <div class="video-btn">
      <svg width="32" height="32" viewBox="0 0 32 32"><circle cx="16" cy="16" r="15" fill="none" stroke="#fff" stroke-width="2"/><polygon points="12,9 24,16 12,23" fill="#fff"/></svg>
      <span>Click Here<br>To Watch Our Video</span>
    </div>
  </a>
  <a class="brochure" href="#">
    <div class="brochure-title">Download<br>Our Brocheure</div>
    <div class="brochure-thumb" role="img" aria-label="Brochure cover with a photo of two seniors and the tagline The care and company you need to be at home"></div>
  </a>

  <article class="topic" style="left:98px;top:878px"><h3>Junior-Seniors Assisting Senior-Seniors</h3><p>Ipsum is simply dummy text of the printing and typesetting industry. Lorem Ipsum has been the industry's standard dummy text ever since the 1500s, when an unknownfhive centuries, but also the leap into.</p></article>
  <article class="topic" style="left:440px;top:878px"><h3>Why non-medical in-home care ?</h3><p>Lorem Ipsum is simply dummy text of the printing and typesetting industry. Lorem Ipsum has been the industry's standard dummy text ever since the 1500s, when an unknownfhive centuries, but also the leap into.</p></article>
  <article class="topic" style="left:782px;top:878px"><h3>Who are junior-seniors?</h3><p>Is simply dummy text of the printing and typesetting industry. Lorem Ipsum has been the industry's standard dummy text ever since the 1500s, when an unknownfhive centuries, but also the leap into.</p></article>
  <a class="btn-learn" href="#" style="left:98px;top:1068px">Learn More</a>
  <a class="btn-learn" href="#" style="left:440px;top:1068px">Learn More</a>
  <a class="btn-learn" href="#" style="left:782px;top:1068px">Learn More</a>

  <article class="topic" style="left:98px;top:1134px"><h3>Financial effects of senior care</h3><p style="margin-top:30px">Simply dummy text of the printing and typesetting industry. Lorem Ipsum has been the industry's standard dummy text ever since the 1500s, when an unknownfhive centuries, but also the leap into.</p></article>
  <article class="topic" style="left:440px;top:1134px"><h3>Do you need care?</h3><p style="margin-top:30px">Dummy text of the printing and typesetting industry. Lorem Ipsum has been the industry's standard dummy text ever since the 1500s, when an unknownfhive centuries, but also the leap into.</p></article>
  <article class="topic" style="left:782px;top:1134px"><h3>Does someone you love need care?</h3><p style="margin-top:10px">Text of the printing and typesetting industry Lorem Ipsum has been the industry's standard dummy text ever since the 1500s, when an unknownfhive centuries, but also the leap into.</p></article>
  <a class="btn-learn" href="#" style="left:98px;top:1324px">Learn More</a>
  <a class="btn-learn" href="#" style="left:440px;top:1324px">Learn More</a>
  <a class="btn-learn" href="#" style="left:782px;top:1324px">Learn More</a>
</section>

<section class="services">
  <h2 class="section-title" style="top:32px">Our Services</h2>
  <div class="rule" style="top:92px;background:rgba(255,255,255,.35)"></div>

  <div class="service" style="left:90px">
    <svg class="hex" width="80" height="80" viewBox="0 0 80 80"><polygon points="40,2 73,21 73,59 40,78 7,59 7,21" fill="#f05a52"/><path d="M29 34h22l-2 20H31z" fill="none" stroke="#fff" stroke-width="2.5"/><path d="M34 34v-4a6 6 0 0 1 12 0v4" fill="none" stroke="#fff" stroke-width="2.5"/></svg>
    <h4>GROCERY SHOPPING</h4>
    <p>Lorem ipsum dolor sit amet cras vitae sodales ac nec prellentesque vivamus</p>
  </div>
  <div class="service" style="left:345px">
    <svg class="hex" width="80" height="80" viewBox="0 0 80 80"><polygon points="40,2 73,21 73,59 40,78 7,59 7,21" fill="#fff"/><rect x="27" y="28" width="26" height="24" fill="none" stroke="#222" stroke-width="2.5"/><path d="M27 35h26M33 24v7M47 24v7" stroke="#222" stroke-width="2.5"/><text x="40" y="48" font-size="10" font-family="Montserrat,sans-serif" font-weight="700" text-anchor="middle" fill="#222">25</text></svg>
    <h4>MEDICAL OR DENTAL<br>APPOINTMENTS</h4>
    <p>Lorem ipsum dolor sit amet cras vitae sodales ac nec prellentesque vivamus</p>
  </div>
  <div class="service" style="left:605px">
    <svg class="hex" width="80" height="80" viewBox="0 0 80 80"><polygon points="40,2 73,21 73,59 40,78 7,59 7,21" fill="#fff"/><rect x="29" y="26" width="22" height="28" fill="none" stroke="#222" stroke-width="2.5"/><path d="M34 34h12M34 40h12M34 46h8" stroke="#222" stroke-width="2.5"/></svg>
    <h4>ERRANDS</h4>
    <p>Lorem ipsum dolor sit amet cras vitae sodales ac nec prellentesque vivamus</p>
  </div>
  <div class="service" style="left:860px">
    <svg class="hex" width="80" height="80" viewBox="0 0 80 80"><polygon points="40,2 73,21 73,59 40,78 7,59 7,21" fill="#fff"/><path d="M26 44a14 14 0 0 1 28 0z" fill="#222"/><path d="M24 47h32" stroke="#222" stroke-width="3"/><circle cx="40" cy="28" r="2.5" fill="#222"/></svg>
    <h4>MEAL PREPARATION &amp; CLEANUP</h4>
    <p>Lorem ipsum dolor sit amet cras vitae sodales ac nec prellentesque vivamus</p>
  </div>

  <div class="dots"><span class="on"></span><span></span><span></span><span></span></div>
</section>

<section class="testimonial">
  <h2 class="section-title" style="top:30px;color:var(--navy)">Testimonial</h2>
  <div class="rule" style="top:88px;background:#ccc"></div>
  <div class="t-photo" role="img" aria-label="Portrait photo of a client in a suit"></div>
  <div class="t-card">
    <p class="t-quote">Lorem Ipsum is simply dummy text of the printing and typesetting industry. Lorem Ipsum has been the industry's standard dummy text ever since the 1500s, when an unknown printer took a galley of type and scrambled it to make a type specimen book. It has survived not only five centuries.</p>
    <div class="t-author"><i></i><b>John Doe ,</b><span>Lorem Ipsum</span></div>
  </div>
</section>

<section class="news">
  <h2 class="section-title" style="top:28px">Recent News</h2>
  <div class="rule" style="top:86px;background:rgba(255,255,255,.35)"></div>
  <div class="news-grid">
    <article class="news-item"><time>22 January,2017</time>Lorem Ipsum is simply dummy text of the printing and typesetting industry. Lorem Ipsum has been the industry's standard dummy text.</article>
    <div class="news-photo" role="img" aria-label="Photo of a smiling senior couple"></div>
    <article class="news-item"><time>22 January,2017</time>Lorem Ipsum is simply dummy text of the printing and typesetting industry. Lorem Ipsum has been the industry's standard dummy text.</article>
    <div class="news-photo b" role="img" aria-label="Photo of a caregiver hugging a senior woman"></div>
    <div class="news-photo c" role="img" aria-label="Photo of two senior women with a basket of groceries"></div>
    <article class="news-item left-arrow"><time>22 January,2017</time>Lorem Ipsum is simply dummy text of the printing and typesetting industry. Lorem Ipsum has been the industry's standard dummy text.</article>
    <div class="news-photo d" role="img" aria-label="Photo of a caregiver helping a senior in the kitchen"></div>
    <article class="news-item left-arrow"><time>22 January,2017</time>Lorem Ipsum is simply dummy text of the printing and typesetting industry. Lorem Ipsum has been the industry's standard dummy text.</article>
  </div>
  <a class="btn-more" href="#">View More</a>
</section>

<section class="contact">
  <h2 class="section-title">CONTACT US</h2>
  <p class="contact-sub">Nullam sit amet odio eu est aliquet euismod a a urna. Proin eu urna suscipit, dictum</p>
  <div class="map" role="img" aria-label="Street map of the service area"></div>
  <form class="contact-form">
    <div class="field" style="top:48px">Name</div>
    <div class="field" style="top:100px">Email</div>
    <div class="field" style="top:152px;height:140px">Message</div>
    <div class="btn-send">Send Message</div>
  </form>
</section>

<footer class="site-footer">
  <div class="footer-h" style="left:98px;top:30px">Quick Links</div>
  <ul class="quick-links">
    <li>Home</li><li>Services</li><li>About Us</li><li>News</li><li>Employment</li><li>Contact Us</li>
  </ul>
  <div class="footer-h" style="left:502px;top:32px">Address</div>
  <div class="address">
    <strong>Willowbrook Elders LLC</strong>
    <div class="contact-line" style="margin-top:6px">
      <svg width="12" height="14" viewBox="0 0 12 14"><path d="M6 0a5 5 0 0 1 5 5c0 4-5 9-5 9S1 9 1 5a5 5 0 0 1 5-5z" fill="#fff"/><circle cx="6" cy="5" r="2" fill="#0e4a8b"/></svg>
      <span>P.O. Box 418, Maple Hollow,<br>New York 12999</span>
    </div>
    <div class="contact-line">
      <svg width="12" height="12" viewBox="0 0 24 24"><path d="M6.6 10.8a15 15 0 0 0 6.6 6.6l2.2-2.2a1 1 0 0 1 1-.25 11 11 0 0 0 3.6.6 1 1 0 0 1 1 1V20a1 1 0 0 1-1 1A17 17 0 0 1 3 4a1 1 0 0 1 1-1h3.5a1 1 0 0 1 1 1c0 1.25.2 2.45.57 3.57a1 1 0 0 1-.25 1z" fill="#fff"/></svg>
      <span>555 - 014 - 2290</span>
    </div>
    <div class="contact-line">
      <svg width="12" height="12" viewBox="0 0 24 24"><rect x="5" y="2" width="14" height="6" fill="#fff"/><rect x="2" y="9" width="20" height="9" rx="1" fill="#fff"/><rect x="6" y="14" width="12" height="8" fill="#fff" stroke="#0e4a8b" stroke-width="1.5"/></svg>
      <span>555 - 014 - 7731</span>
    </div>
  </div>
  <div class="footer-brand"><span class="brand-square"></span><span class="brand-name">Willowbrook Elders</span></div>
</footer>
<div class="copyright">Copyright 2017. Willowbrook Elders LLC. All rights reserved</div>

</body>
</html>
```